Driftwood Sailing. Explore the Whitsundays We Dare You

Hello,
I have a catamaran charter business in the Whitsunday Islands, Australia.
My business is called Driftwood Sailing and my catamaran is a Maristo 380 K4 and his name is Quiet Tern. I have attached its logo but would like something for Driftwood Sailing.
I am looking for a website for my business.
I'm also after 1 logos (for Driftwood Sailing).
I would like to be able to edit the website if needed (putting photos into the gallery, post reviews) and I'll need a shopping cart and all the usual social media contacts.
I will also need a live availability calendar for people to look at to see if the dates they want are available. I will need to easily edit this.
It must also stand out. I can supply most of the picture and maybe some video.
There will only be about 7 pages -
Home - Pictures scrolling past
Price and Availability - Have to show a live calendar that people can click on to see if the dates they want are available.
Gallery - I will put up photos and comments from past charterers.
Contact - A form they fill out to ask questions
Testimonials & Reviews - People can submit photos and review. I will have to be able to easily edit them.
Bookings & Store - If they want to pay by card, or if they want to buy any merchandise and so it would need a shopping cart.
Misc Page - What to bring, What to expect, etc etc
At the moment I only have 1 catamaran that will be advertised but I may get another at a later date.
The site will need a chilled out feel as people will be coming to the Whitsundays to relax and sail around.
The font needs to be a friendly font if this is possible.
The photo I uploaded called Anchor Tattoo is the logo I want for Driftwood Sailing.
Hope this helps.
Does this sound do-able

Target Market(s)

20 - 60

Industry/Entity Type

Tourism

Coding

Coded - Design and coding required

Number of Pages Required

5+ page

Colors

Designer to choose colors to be used in the design.

Requirements
Must have
• Chilled out feel

```html
<!DOCTYPE html>
<html lang="en">
<head>
<meta charset="utf-8">
<title>Quiet Tern – Whitsunday Catamaran Charter</title>
<link href="https://fonts.googleapis.com/css2?family=Open+Sans:wght@400;600;700&family=Raleway:wght@300;400;600;700;800&display=swap" rel="stylesheet">
<style>
:root{
  --orange:#e8643a;
  --orange-dark:#c9502a;
  --navy:#1c4a66;
  --navy-deep:#12344a;
  --ink:#222a30;
  --text:#5b6166;
  --muted:#9aa0a5;
  --light:#eeeeee;
  --white:#ffffff;
  --green:#7cb342;
  --red:#ef5b4d;
}
*{box-sizing:border-box;margin:0;padding:0}
html,body{width:1200px;height:5143px;overflow:hidden}
body{position:relative;background:var(--white);font-family:"Open Sans",Arial,sans-serif;color:var(--text)}
.abs{position:absolute}
.heading{font-family:"Raleway",Arial,sans-serif}
.btn{position:absolute;display:inline-block;background:var(--orange);color:var(--white);font-family:"Raleway",Arial,sans-serif;font-weight:700;font-size:15px;letter-spacing:.5px;padding:9px 22px;border-radius:4px;text-transform:uppercase}
.btn-round{border-radius:20px}
.brand{display:flex;align-items:center;gap:10px;font-family:"Raleway",Arial,sans-serif;font-weight:700;color:var(--ink)}
.brand-dot{width:18px;height:18px;border-radius:50%;background:var(--orange)}

/* header */
.site-header{left:0;top:0;width:1200px;height:130px;background:var(--white)}
.site-header .brand{left:130px;top:38px;font-size:34px}
.header-phone{left:632px;top:30px;font-size:16px;color:var(--ink);display:flex;align-items:center;gap:8px}
.header-phone b{color:var(--orange)}
.site-header .btn{left:940px;top:23px;font-size:13px;padding:7px 14px}
.main-nav{right:135px;top:82px;display:flex;gap:26px;font-family:"Raleway",Arial,sans-serif;font-weight:700;font-size:14px;color:var(--ink)}

/* hero */
.hero{left:0;top:130px;width:1200px;height:640px;background:linear-gradient(160deg,#3b5b6e 0%,#1f3d52 45%,#2d5a78 75%,#18324a 100%)}
.hero-curve{left:0;top:600px}
.hero-title{left:0;width:1200px;top:245px;text-align:center;color:var(--white);font-family:"Raleway",Arial,sans-serif;font-weight:800;font-size:54px;letter-spacing:1px}
.hero-sub{left:0;width:1200px;top:320px;text-align:center;color:#e8eef2;font-size:16px;line-height:24px}
.hero .btn{left:542px;top:395px}
.hero-dots{left:574px;top:470px;display:flex;gap:9px}
.hero-dots i{width:9px;height:9px;border-radius:50%;background:var(--white);opacity:.7}
.hero-dots i:first-child{opacity:1}

/* welcome */
.deckplan{left:50px;top:885px;width:420px;height:285px;background:linear-gradient(90deg,#f3f3f3,#e2d6c4 50%,#f3f3f3);border-radius:6px}
.welcome-kicker{left:612px;top:880px;color:var(--orange);font-family:"Raleway",Arial,sans-serif;font-size:26px;font-weight:400}
.welcome-title{left:612px;top:912px;color:var(--ink);font-family:"Raleway",Arial,sans-serif;font-size:36px;font-weight:800}
.welcome-text{left:612px;top:975px;width:520px;font-size:13px;line-height:24px}
.welcome .btn{left:612px;top:1125px}

/* gallery */
.gallery{left:0;top:1300px;width:1200px;height:1005px;background:var(--light)}
.section-title{width:1200px;left:0;text-align:center;font-family:"Raleway",Arial,sans-serif}
.gallery-title{top:75px;color:var(--orange);font-size:56px;font-weight:800}
.gallery-sub{top:148px;color:var(--ink);font-size:24px;font-weight:400}
.tile{position:absolute}
.tile-card{position:absolute;left:443px;top:1970px;width:313px;height:190px;background:var(--white);padding:22px 24px}
.tile-card .place{color:var(--orange);font-size:15px;font-family:"Raleway",Arial,sans-serif}
.tile-card h3{font-family:"Raleway",Arial,sans-serif;font-weight:800;font-size:25px;line-height:30px;color:var(--ink);margin-top:4px}
.tile-card .more{font-size:12px;font-weight:700;color:var(--ink);margin-top:10px}

/* price */
.price{left:0;top:2305px;width:1200px;height:800px;background:linear-gradient(180deg,#123a52 0%,#1b5a72 50%,#0e3146 100%)}
.price-kicker{top:60px;color:var(--white);font-size:28px;font-weight:300}
.price-title{top:100px;color:var(--white);font-size:44px;font-weight:800}
.calendar-card{left:216px;top:2505px;width:769px;height:480px;background:var(--white);border-radius:4px;box-shadow:0 10px 30px rgba(0,0,0,.35)}
.cal-head{left:55px;top:36px;width:505px;display:flex;justify-content:space-between;align-items:center;font-family:"Raleway",Arial,sans-serif}
.cal-head .yr{color:var(--orange);font-size:14px}
.cal-head .month{color:var(--ink);font-size:20px;font-weight:600}
.cal-grid{left:50px;top:115px;width:520px;display:grid;grid-template-columns:repeat(7,1fr);row-gap:15px;text-align:center;font-size:14px;color:var(--ink)}
.cal-grid .dow{font-family:"Raleway",Arial,sans-serif;font-weight:800;font-size:16px;margin-bottom:10px}
.cal-grid span{display:inline-block;width:28px;height:28px;line-height:28px;margin:0 auto;border-radius:50%}
.cal-grid .free{background:var(--green);color:var(--white)}
.cal-grid .busy{background:var(--red);color:var(--white)}
.cal-arrow{width:18px;height:18px;border-radius:50%;background:var(--red)}
.legend{top:405px;display:inline-block;color:var(--white);font-family:"Raleway",Arial,sans-serif;font-weight:700;font-size:14px;padding:7px 20px;border-radius:4px}
.sidebar{left:600px;top:30px;width:150px}
.sidebar .brand{font-size:20px}
.side-list{margin-top:40px;list-style:none}
.side-list li{font-family:"Raleway",Arial,sans-serif;font-weight:700;font-size:12px;color:var(--ink);letter-spacing:1px;padding:12px 0 12px 10px;border-bottom:2px solid var(--ink)}
.side-btn{top:395px;font-size:12px;padding:7px 14px;border-radius:3px;color:var(--white);font-family:"Raleway",Arial,sans-serif;font-weight:700}

/* testimonials */
.testimonials{left:0;top:3105px;width:1200px;height:575px;background:linear-gradient(180deg,#d96a34 0%,#c4531f 55%,#b24b1e 100%)}
.testi-title{top:100px;color:var(--white);font-size:38px;font-weight:800}
.testi-card{position:absolute;top:240px;width:275px;height:157px;background:var(--white);border-radius:8px;padding:60px 26px 0;font-size:12px;line-height:19px;color:var(--text);box-shadow:0 8px 18px rgba(0,0,0,.2)}
.testi-card b{color:var(--ink);font-size:22px;font-family:Georgia,serif}
.avatar{position:absolute;top:185px;width:90px;height:90px;border-radius:50%;border:5px solid var(--white);background:linear-gradient(#8a6b55,#3f2f27)}
.testi-name{position:absolute;top:415px;width:275px;text-align:center;color:var(--white);font-family:"Raleway",Arial,sans-serif;font-weight:600;font-size:15px}
.stars{position:absolute;top:448px;width:275px;text-align:center;color:var(--white);font-size:16px;letter-spacing:3px}

/* premier */
.premier-title{left:130px;top:3845px;width:480px;color:var(--ink);font-family:"Raleway",Arial,sans-serif;font-weight:800;font-size:28px;line-height:36px}
.premier-title em{font-style:normal;color:var(--orange)}
.premier-text{left:130px;top:3975px;width:490px;font-size:13px;line-height:22px}
.premier .btn{left:130px;top:4075px;border-radius:3px}
.yacht-photo{left:670px;top:3840px;width:410px;height:290px;background:linear-gradient(180deg,#a9c9e6 0%,#dce9f3 55%,#7a8f9a 80%,#506a78 100%)}
.frame{left:655px;top:3825px;width:440px;height:320px}

/* store */
.store-band{left:0;top:4290px}
.store-photo{left:103px;top:4335px;width:400px;height:400px;border-radius:50%;border:6px solid var(--white);background:radial-gradient(circle at 50% 40%,#f2f2f2 0%,#cfd4d8 55%,#6c7e8a 100%)}
.store-title{left:595px;top:4390px;color:var(--white);font-family:"Raleway",Arial,sans-serif;font-weight:800;font-size:38px}
.store-text{left:595px;top:4455px;width:470px;color:#d9e6ee;font-size:13px;line-height:22px}
.store-price{left:595px;top:4570px;color:var(--white);font-family:"Raleway",Arial,sans-serif;font-weight:700;font-size:18px}
.store .btn{left:595px;top:4625px;border-radius:3px}

/* footer */
.footer-head{top:4818px;color:var(--ink);font-family:"Raleway",Arial,sans-serif;font-weight:800;font-size:18px}
.contact-list{left:108px;top:4865px;list-style:none;font-size:12px;line-height:18px;color:var(--text)}
.contact-list li{display:flex;gap:10px;margin-bottom:14px}
.news-text{left:388px;top:4860px;width:290px;font-size:11px;line-height:17px}
.news-input{left:388px;top:4905px;width:275px;height:36px;border:1px solid #ccc;font-size:11px;color:var(--muted);padding:10px}
.footer-links{left:740px;top:4862px;list-style:disc;padding-left:14px;font-size:12px;line-height:19px;color:var(--ink)}
.footer-brand{left:895px;top:4880px;font-size:24px}
.socials{left:950px;top:4940px;display:flex;gap:7px}
.socials i{width:22px;height:22px;border-radius:50%;border:2px solid var(--ink)}
.copyright{left:0;top:5080px;width:1200px;border-top:1px solid #ddd;padding-top:20px;text-align:center;font-size:11px;color:var(--ink)}
</style>
</head>
<body>

<header class="site-header abs">
  <div class="brand abs"><span class="brand-dot"></span>Quiet Tern</div>
  <div class="header-phone abs">
    <svg width="18" height="18" viewBox="0 0 24 24"><path fill="#e8643a" d="M6.6 10.8a15 15 0 0 0 6.6 6.6l2.2-2.2c.3-.3.7-.4 1-.2 1.1.4 2.3.6 3.6.6.6 0 1 .4 1 1V20c0 .6-.4 1-1 1A17 17 0 0 1 3 4c0-.6.4-1 1-1h3.5c.6 0 1 .4 1 1 0 1.3.2 2.5.6 3.6.1.3 0 .7-.2 1z"/></svg>
    <span>Call Us: <b>(+1) 555-014-2290</b></span>
  </div>
  <span class="btn">Book Online</span>
  <nav class="main-nav abs">
    <span>HOME</span><span>PRICE &amp; AVAILABILITY</span><span>GALLERY</span><span>TESTIMONIALS</span><span>BOOKINGS &amp; STORE</span><span>MISC</span>
  </nav>
</header>

<section class="hero abs" role="img" aria-label="Guests relaxing on the deck of the catamaran at sea">
  <svg class="hero-curve abs" width="1200" height="40" viewBox="0 0 1200 40"><path d="M0 0 Q600 80 1200 0 V40 H0z" fill="#ffffff"/></svg>
  <h1 class="hero-title abs">QUIET TERN</h1>
  <p class="hero-sub abs">Sail calm island waters aboard our catamaran and let the<br>Whitsundays slow your days to an easy pace.</p>
  <span class="btn btn-round">Read More</span>
  <div class="hero-dots abs"><i></i><i></i><i></i><i></i></div>
</section>

<section class="welcome">
  <div class="deckplan abs" role="img" aria-label="Deck plan drawing of the Maristo 380 K4 catamaran"></div>
  <div class="welcome-kicker abs">WELCOME TO</div>
  <h2 class="welcome-title abs">QUIET TERN</h2>
  <p class="welcome-text abs">Quiet Tern is a roomy Maristo 380 K4 catamaran built for slow days among the islands. Drop anchor in sheltered bays, swim over the reef, walk white sand beaches and watch the sun set from the deck. We look after the sailing and the details so you can simply unwind and enjoy time together on the water.</p>
  <span class="btn btn-round">Read More</span>
</section>

<section class="gallery abs">
  <h2 class="section-title gallery-title abs">GALLERY</h2>
  <p class="section-title gallery-sub abs">QUIET TERN</p>
</section>
<div class="tile" style="left:130px;top:1533px;width:313px;height:312px;background:linear-gradient(160deg,#6d8f4a,#2d5a78)" role="img" aria-label="Flag and life ring on the catamaran stern"></div>
<div class="tile" style="left:443px;top:1533px;width:313px;height:312px;background:linear-gradient(180deg,#2f8fb0,#1a5f82)" role="img" aria-label="Snorkeller swimming underwater"></div>
<div class="tile" style="left:756px;top:1533px;width:310px;height:312px;background:linear-gradient(170deg,#6b8fa3,#3f4d55)" role="img" aria-label="Two guests smiling aboard"></div>
<div class="tile" style="left:130px;top:1845px;width:313px;height:315px;background:linear-gradient(180deg,#3a9ac4,#1e6a96)" role="img" aria-label="Sea turtle swimming in clear water"></div>
<div class="tile" style="left:443px;top:1845px;width:313px;height:125px;background:linear-gradient(180deg,#5aa6c8,#8fb7c9)" role="img" aria-label="Guest on deck in sunshine"></div>
<div class="tile" style="left:756px;top:1845px;width:310px;height:315px;background:linear-gradient(180deg,#5c8fb4,#3c6078)" role="img" aria-label="Group relaxing on the trampoline deck"></div>
<div class="tile-card">
  <div class="place">AUSTRALIA</div>
  <h3>QUIS AUTEM VEL EUM IURE REPREHENDERIT</h3>
  <div class="more">› FIND OUT MORE</div>
</div>

<section class="price abs" role="region" aria-label="Price and availability">
  <div class="abs" style="left:0;top:0;width:1200px;height:800px" role="img" aria-label="Underwater reef scene behind the calendar"></div>
  <p class="section-title price-kicker abs heading">Quiet Tern</p>
  <h2 class="section-title price-title abs">PRICE AND AVAILABILITY</h2>
</section>

<div class="calendar-card abs">
  <div class="cal-head abs"><span class="yr">2017</span><span class="month">MARCH, 2018</span><span class="yr">2019</span></div>
  <div class="cal-arrow abs" style="left:18px;top:233px"></div>
  <div class="cal-arrow abs" style="left:578px;top:233px"></div>
  <div class="cal-grid abs">
    <div class="dow">SUN</div><div class="dow">MON</div><div class="dow">TUE</div><div class="dow">WED</div><div class="dow">THUR</div><div class="dow">FRI</div><div class="dow">SAT</div>
    <span></span><span></span><span></span><span></span><span>1</span><span>2</span><span>3</span>
    <span>4</span><span>5</span><span>6</span><span>7</span><span>8</span><span class="free">9</span><span>10</span>
    <span>11</span><span>12</span><span class="busy">13</span><span>14</span><span>15</span><span>16</span><span>17</span>
    <span>18</span><span>19</span><span>20</span><span>21</span><span class="free">22</span><span>23</span><span>24</span>
    <span>25</span><span>26</span><span>27</span><span>28</span><span>29</span><span>30</span><span>31</span>
  </div>
  <span class="legend abs" style="left:70px;background:var(--green)">AVAILABLE</span>
  <span class="legend abs" style="left:195px;background:var(--red)">CANCELLED</span>
  <div class="sidebar abs">
    <div class="brand"><span class="brand-dot"></span>Quiet Tern</div>
    <ul class="side-list">
      <li>NEMO ENIM IPSAM</li><li>NEMO ENIM IPSAM</li><li>NEMO ENIM IPSAM</li><li>NEMO ENIM IPSAM</li><li>NEMO ENIM IPSAM</li>
    </ul>
  </div>
  <span class="side-btn abs" style="left:600px;background:var(--ink)">READ MORE</span>
  <span class="side-btn abs" style="left:700px;background:var(--orange);padding:7px 10px">›</span>
</div>

<section class="testimonials abs" role="region" aria-label="Testimonials">
  <h2 class="section-title testi-title abs">TESTIMONIALS</h2>
  <div class="avatar" style="left:248px" role="img" aria-label="Guest portrait"></div>
  <div class="testi-card" style="left:155px"><b>“</b> The crew made every day easy. We swam, sailed and ate well, and left feeling rested and happy.</div>
  <div class="testi-name" style="left:155px">Mara – Quiet Tern</div>
  <div class="stars" style="left:155px">★★★★★</div>
  <div class="avatar" style="left:556px" role="img" aria-label="Guest portrait"></div>
  <div class="testi-card" style="left:463px"><b>“</b> A calm, beautiful week among the islands. The boat was spotless and the anchorages were stunning.</div>
  <div class="testi-name" style="left:463px">Mara – Quiet Tern</div>
  <div class="stars" style="left:463px">★★★★★</div>
  <div class="avatar" style="left:865px" role="img" aria-label="Guest portrait"></div>
  <div class="testi-card" style="left:772px"><b>“</b> Turtles, reef and sunsets every night. We are already planning our next charter on board.</div>
  <div class="testi-name" style="left:772px">Mara – Quiet Tern</div>
  <div class="stars" style="left:772px">★★★★★</div>
</section>

<section class="premier">
  <h2 class="premier-title abs">THE PREMIER CHOICE FOR YOUR <em>WHITSUNDAY</em> YACHT QUIET TERN EXPERIENCE.</h2>
  <p class="premier-text abs">Charter a spacious catamaran with an easygoing crew and discover quiet bays, warm water and island walks. Every trip is planned around your pace, with fresh meals, snorkel gear and plenty of shade on deck for lazy afternoons.</p>
  <span class="btn">Book Now</span>
  <svg class="frame abs" width="440" height="320" viewBox="0 0 440 320" fill="none" stroke="#3a3f44" stroke-width="2">
    <path d="M1 40V1H40M400 1H439V40M439 280V319H400M40 319H1V280"/>
  </svg>
  <div class="yacht-photo abs" role="img" aria-label="Quiet Tern catamaran moored in a marina"></div>
</section>

<section class="store">
  <svg class="store-band abs" width="1200" height="500" viewBox="0 0 1200 500"><path d="M0 60 L1200 0 V440 L0 495z" fill="#1c4a66"/></svg>
  <div class="store-photo abs" role="img" aria-label="White branded t-shirt from the store"></div>
  <h2 class="store-title abs">OUR STORE</h2>
  <p class="store-text abs">Take a little of the islands home. Our soft cotton tees, caps and drink bottles are made for sunny days on deck and easy evenings ashore. Order online and collect on board.</p>
  <div class="store-price abs">$20.00</div>
  <span class="btn">Shop Now</span>
</section>

<footer>
  <h3 class="footer-head abs" style="left:108px">CONTACT US</h3>
  <ul class="contact-list abs">
    <li><svg width="12" height="16" viewBox="0 0 12 16"><path fill="#e8643a" d="M6 0a6 6 0 0 0-6 6c0 4.5 6 10 6 10s6-5.5 6-10a6 6 0 0 0-6-6zm0 8.5A2.5 2.5 0 1 1 6 3.5a2.5 2.5 0 0 1 0 5z"/></svg><span>Quiet Tern, Berth 12, Coral Marina<br>Airlie Beach QLD 4802</span></li>
    <li><svg width="12" height="14" viewBox="0 0 24 24"><path fill="#e8643a" d="M6.6 10.8a15 15 0 0 0 6.6 6.6l2.2-2.2c.3-.3.7-.4 1-.2 1.1.4 2.3.6 3.6.6.6 0 1 .4 1 1V20c0 .6-.4 1-1 1A17 17 0 0 1 3 4c0-.6.4-1 1-1h3.5c.6 0 1 .4 1 1 0 1.3.2 2.5.6 3.6.1.3 0 .7-.2 1z"/></svg><span>Phone: (+1) 555-014-2290</span></li>
    <li><svg width="14" height="12" viewBox="0 0 14 12"><rect x="0.5" y="0.5" width="13" height="11" fill="none" stroke="#e8643a"/><path d="M0.5 0.5L7 6l6.5-5.5" fill="none" stroke="#e8643a"/></svg><span>Email: hello@quiettern-sail.test</span></li>
  </ul>
  <h3 class="footer-head abs" style="left:388px">SIGN UP FOR NEWSLETTER</h3>
  <p class="news-text abs">Get sailing news, seasonal offers and new gallery photos sent straight to your inbox each month.</p>
  <div class="news-input abs">Enter email</div>
  <span class="btn" style="left:388px;top:4958px;font-size:12px;padding:7px 16px;border-radius:3px">Sign Up</span>
  <h3 class="footer-head abs" style="left:740px">QUICK LINKS</h3>
  <ul class="footer-links abs">
    <li>Home</li><li>Price &amp; Availability</li><li>Gallery</li><li>Testimonials</li><li>Bookings &amp; Store</li><li>Misc</li>
  </ul>
  <div class="brand footer-brand abs"><span class="brand-dot"></span>Quiet Tern</div>
  <div class="socials abs"><i></i><i></i><i></i><i></i></div>
  <div class="copyright abs">© Copyright 2017 Quiet Tern - All Rights Reserved.</div>
</footer>

</body>
</html>
```